Veltrane Hand Sanitiser Spray Product Range for International Markets

Veltrane is a new Healthcare business launching a full product range of Anti-bacterial Hand Sanitiser Spray bottles in various sizes. We have a new logo which we believe differentiates us from the competition: Veltrane - Care That Goes Further
The Product Range will comprise two distinct product solution types:
- Anti-bacterial Hand Sanitisers - Alcohol based
- Anti-bacterial Hand Sanitisers - Sensitive Non Alcohol based
Bottle sizes will comprise a range containing:
100ml, 250ml, 500ml, 1ltr, 5ltr, 10ltr
Some bottles will have Pump Sprays
The Product labelling will be attractive front packaging label combined with strong product attributes and usage indicator cues.
As a Healthcare brand our logo design is light Green. We believe that this should be combined with blues and greens balanced to create contrast and strong stand-out on-shelf.
A review of competitor brands will show some similar colour cues, however as a Healthcare brand, the colour cues Green and White are synonymous with the sector. Many existing brands are very pragmatic in their label design. i.e. #it does what is says on the tin approach#. Our brand will need strong stand-out and strong aesthetic appeal too, since it will often be left in public view and around the home and office and therefore should look as attractive as possible. There will be other brand variants in the future and thought should be given to this too - with use of colour cues.
For Competitor indicators check-out the brands on Brisklot - Pine Hollow, Dermavell and others....Thank-you!

Target Market(s)

First: Female 25 - 65
Second: Male 25 - 65

Contact Information for Business Card

Garth L. Dunmore
CEO
Veltrane Healthcare Worldwide
'Care That Goes Further'
www.VeltraneHealthcare.example
E. gldunmore@veltranehealthcare.example
T. +44 7700 900318
T. +44 118 496072

Font styles to use
Sans Serif

Colors
34a7d7
33b8a4
add136
fbee3e
b768aa

```html
<!DOCTYPE html>
<html lang="en">
<head>
<meta charset="utf-8">
<title>Veltrane Hand Sanitizer Labels</title>
<link rel="stylesheet" href="https://fonts.googleapis.com/css2?family=Tenor+Sans&family=Oswald:wght@500;600&family=Open+Sans:wght@400;600;700&family=PT+Sans+Narrow:wght@400;700&display=swap">
<style>
:root{
  --bg:#f4f4f4;
  --white:#ffffff;
  --ink:#333a3f;
  --muted:#555b60;
  --blue:#1e9fce;
  --teal:#12a88c;
  --purple:#6b3f98;
  --green:#8cc63f;
  --lime:#add136;
  --icon:#7dbd3a;
}
*{margin:0;padding:0;box-sizing:border-box}
html,body{width:1200px;height:927px;overflow:hidden;background:var(--bg)}
body{position:relative;font-family:"Open Sans",Arial,sans-serif;color:var(--ink)}
.label{position:absolute;top:325px;width:228px;height:410px;background:var(--white);border-radius:14px;overflow:hidden;box-shadow:0 2px 8px rgba(0,0,0,.08)}
.label--blue{left:120px}
.label--purple{left:498px}
.label--teal{left:838px}
.pattern-top{position:absolute;left:0;top:0;width:100%;height:165px;clip-path:polygon(0 0,100% 0,100% 52%,50% 100%,0 52%)}
.label--blue .pattern-top,.label--teal .pattern-top{background:linear-gradient(160deg,#1fa9d8 0%,#2fbfa6 40%,#6cc66a 75%,#b6d84a 100%)}
.label--purple .pattern-top{background:linear-gradient(120deg,#27b2d6 0%,#3fbf77 25%,#e9e43a 50%,#f08a2a 70%,#d8347f 88%,#8b3fa0 100%)}
.logo-frame{position:absolute;left:44px;top:26px;width:140px;height:92px;border:1.5px solid rgba(255,255,255,.9)}
.brand{position:absolute;left:0;top:46px;width:100%;text-align:center;font-family:"Tenor Sans",Arial,sans-serif;font-size:29px;color:var(--white);letter-spacing:.3px}
.tagline{position:absolute;left:0;top:92px;width:100%;text-align:center;font-size:6.5px;color:var(--white)}
.kicker{position:absolute;left:0;top:174px;width:100%;text-align:center;font-size:9px;font-weight:600;letter-spacing:1px;color:var(--teal)}
.kicker::before,.kicker::after{content:"";display:inline-block;width:28px;height:1px;background:var(--teal);vertical-align:middle;margin:0 6px}
.band{position:absolute;left:0;top:172px;width:100%;height:38px;display:flex;align-items:center;justify-content:center;font-family:"Oswald",Arial,sans-serif;font-weight:600;font-size:25px;color:var(--white);letter-spacing:.3px}
.label--blue .band{background:var(--blue)}
.label--purple .band{background:var(--purple)}
.label--teal .band{background:var(--teal);top:190px}
.attributes{position:absolute;left:8px;top:220px;width:212px;display:flex;justify-content:space-around;list-style:none}
.label--teal .attributes{top:238px}
.attribute{width:50px;text-align:center;font-size:5.5px;font-weight:600;line-height:1.25}
.attribute .icon{display:block;margin:0 auto 3px;width:28px;height:28px;border-radius:50%;background:var(--icon);border:2px solid #d6ecc0;box-shadow:inset 0 0 0 3px #fff}
.benefits{position:absolute;left:36px;top:292px;list-style:none;font-family:"PT Sans Narrow","Arial Narrow",sans-serif;font-size:9px;font-weight:700;line-height:1.2;z-index:2}
.label--teal .benefits{left:37px;top:306px;font-weight:400;color:var(--muted)}
.benefits li{display:flex;align-items:center;gap:5px;margin-bottom:3px;white-space:nowrap}
.pattern-corner{position:absolute;left:0;bottom:0;width:100%;height:108px;clip-path:polygon(100% 0,100% 100%,0 100%)}
.label--blue .pattern-corner,.label--teal .pattern-corner{background:linear-gradient(135deg,#9fd24a 0%,#3fbf8e 55%,#1fa9c8 100%)}
.label--purple .pattern-corner{left:60px;width:168px;background:linear-gradient(135deg,#f4a12b 0%,#e8423a 45%,#c2318f 75%,#7b3a9c 100%)}
.drop{position:absolute;left:140px;top:282px;width:46px;height:84px;border-radius:50% 50% 50% 50%/40% 40% 60% 60%;background:radial-gradient(circle at 45% 60%,#e6f6fd 0%,#6cc3ea 55%,#1877b8 100%)}
.shield{position:absolute;left:146px;top:290px;width:58px;height:66px;clip-path:polygon(50% 0,100% 22%,100% 70%,50% 100%,0 70%,0 22%);background:radial-gradient(circle at 50% 50%,#eaf8ff 0%,#8fd3e8 60%,#1aa58e 100%)}
.seals{position:absolute;left:14px;top:362px;display:flex;gap:6px}
.seal{width:24px;height:24px;border-radius:50%;background:#2e7fa6;border:2px solid #cfd8dc}
.volume{position:absolute;right:32px;top:378px;font-size:13px;font-weight:700;color:var(--white)}
.label--teal .volume{right:36px;top:372px}
</style>
</head>
<body>

<section class="label label--blue">
  <div class="pattern-top" role="img" aria-label="Blue and green triangle mosaic pattern"></div>
  <div class="logo-frame"></div>
  <div class="brand">Veltrane</div>
  <div class="tagline">Care That Goes Further</div>
  <div class="band">HAND SANITIZER</div>
  <ul class="attributes">
    <li class="attribute"><span class="icon"></span>Skin<br>Friendly</li>
    <li class="attribute"><span class="icon"></span>80% Alcohol<br>Content</li>
    <li class="attribute"><span class="icon"></span>Bio-Based</li>
    <li class="attribute"><span class="icon"></span>Kills 99.99%<br>Germs &amp; Bacteria</li>
  </ul>
  <div class="pattern-corner" role="img" aria-label="Green and blue triangle mosaic corner"></div>
  <div class="drop" role="img" aria-label="Water drop with hand and medical cross illustration"></div>
  <ul class="benefits">
    <li><svg width="8" height="7" viewBox="0 0 8 7"><path d="M1 3.5 3 5.5 7 1" fill="none" stroke="#333a3f" stroke-width="1.4"/></svg>Ethyl Alcohol Antiseptic</li>
    <li><svg width="8" height="7" viewBox="0 0 8 7"><path d="M1 3.5 3 5.5 7 1" fill="none" stroke="#333a3f" stroke-width="1.4"/></svg>Surgical/Medical Grade</li>
    <li><svg width="8" height="7" viewBox="0 0 8 7"><path d="M1 3.5 3 5.5 7 1" fill="none" stroke="#333a3f" stroke-width="1.4"/></svg>Fragrance Free</li>
  </ul>
  <div class="seals"><span class="seal"></span><span class="seal"></span></div>
  <div class="volume">500ml</div>
</section>

<section class="label label--purple">
  <div class="pattern-top" role="img" aria-label="Rainbow triangle mosaic pattern"></div>
  <div class="logo-frame"></div>
  <div class="brand">Veltrane</div>
  <div class="tagline">Care That Goes Further</div>
  <div class="band">HAND SANITIZER</div>
  <ul class="attributes">
    <li class="attribute"><span class="icon"></span>Skin<br>Friendly</li>
    <li class="attribute"><span class="icon"></span>80% Alcohol<br>Content</li>
    <li class="attribute"><span class="icon"></span>Bio-Based</li>
    <li class="attribute"><span class="icon"></span>Kills 99.99%<br>Germs &amp; Bacteria</li>
  </ul>
  <div class="pattern-corner" role="img" aria-label="Orange, pink and purple triangle mosaic corner"></div>
  <div class="drop" role="img" aria-label="Water drop with hand and medical cross illustration"></div>
  <ul class="benefits">
    <li><svg width="8" height="7" viewBox="0 0 8 7"><path d="M1 3.5 3 5.5 7 1" fill="none" stroke="#333a3f" stroke-width="1.4"/></svg>Ethyl Alcohol Antiseptic</li>
    <li><svg width="8" height="7" viewBox="0 0 8 7"><path d="M1 3.5 3 5.5 7 1" fill="none" stroke="#333a3f" stroke-width="1.4"/></svg>Surgical/Medical Grade</li>
    <li><svg width="8" height="7" viewBox="0 0 8 7"><path d="M1 3.5 3 5.5 7 1" fill="none" stroke="#333a3f" stroke-width="1.4"/></svg>Fragrance Free</li>
  </ul>
  <div class="seals"><span class="seal"></span><span class="seal"></span></div>
  <div class="volume">500ml</div>
</section>

<section class="label label--teal">
  <div class="pattern-top" role="img" aria-label="Blue and green triangle mosaic pattern"></div>
  <div class="logo-frame"></div>
  <div class="brand">Veltrane</div>
  <div class="tagline">Care That Goes Further</div>
  <div class="kicker">ANTI-BACTERIAL</div>
  <div class="band">HAND SANITIZER</div>
  <ul class="attributes">
    <li class="attribute"><span class="icon"></span>Skin<br>Friendly</li>
    <li class="attribute"><span class="icon"></span>80% Alcohol<br>Content</li>
    <li class="attribute"><span class="icon"></span>Bio-Based</li>
    <li class="attribute"><span class="icon"></span>Kills 99.99%<br>Germs &amp; Bacteria</li>
  </ul>
  <div class="pattern-corner" role="img" aria-label="Green and blue triangle mosaic corner"></div>
  <div class="shield" role="img" aria-label="Shield with hand and medical cross illustration"></div>
  <ul class="benefits">
    <li><svg width="8" height="7" viewBox="0 0 8 7"><path d="M1 3.5 3 5.5 7 1" fill="none" stroke="#555b60" stroke-width="1.4"/></svg>Ethyl Alcohol Antiseptic</li>
    <li><svg width="8" height="7" viewBox="0 0 8 7"><path d="M1 3.5 3 5.5 7 1" fill="none" stroke="#555b60" stroke-width="1.4"/></svg>Surgical/Medical Grade</li>
    <li><svg width="8" height="7" viewBox="0 0 8 7"><path d="M1 3.5 3 5.5 7 1" fill="none" stroke="#555b60" stroke-width="1.4"/></svg>Fragrance Free</li>
  </ul>
  <div class="volume">500ml</div>
</section>

</body>
</html>
```